GILDED BRICKWORK: THE DEPENDABLE ROUTE WHEREBY MODEST HOUSING FLIPS YIELD HANDSOME RETURNS

I am looking for a book cover design for my new E-Book.

My idea for the design is a pin board with before and after photos of our properties pinned on it (example attached). I have also attached some photos to use.

PLEASE SUBMIT OTHER DESIGNS ALSO AS THIS WAS JUST AN IDEA BUT I AM OPEN TO OTHER IDEAS ALSO.

Page size is 5x7 inches

Font styles to use
Serif
Sans Serif

Colors
0255a3
3176b5
85acd3
85cae6
33a6d7
0392cd
9bcb3c
abd036
ec1f27

```html
<!DOCTYPE html>
<html lang="en">
<head>
<meta charset="utf-8">
<title>Gilded Brickwork – E-Book Cover</title>
<link rel="stylesheet" href="https://fonts.googleapis.com/css2?family=Noto+Serif:wght@400&family=Open+Sans:wght@400&family=Permanent+Marker&display=swap">
<style>
  :root{
    --cover-blue:#1d4fa3;
    --cover-blue-deep:#143c86;
    --cover-blue-light:#2a62b8;
    --cream:#f4efe2;
    --white:#ffffff;
    --paper:#f3f3f3;
    --rule:#b9bcc2;
    --ink:#1f2a44;
    --alert-red:#ec1f27;
  }
  *{margin:0;padding:0;box-sizing:border-box}
  html,body{width:923px;height:1200px;overflow:hidden;background:var(--cover-blue-deep)}
  .cover{
    position:relative;width:923px;height:1200px;overflow:hidden;
    background:radial-gradient(ellipse at 50% 45%,var(--cover-blue-light) 0%,var(--cover-blue) 55%,var(--cover-blue-deep) 100%);
    font-family:"Noto Serif",Georgia,serif;color:var(--cream);
  }
  .author{position:absolute;top:68px;left:0;width:100%;text-align:center;font-size:31px;letter-spacing:5px;font-weight:400}
  .book-title{font-weight:400}
  .title{position:absolute;left:0;width:100%;text-align:center;line-height:1;font-weight:400}
  .title-main{top:108px;font-size:82px;letter-spacing:5px}
  .title-sub{top:186px;font-size:58px;letter-spacing:20px;padding-left:20px}

  .snap{position:absolute;background:var(--white);padding:5px;box-shadow:3px 4px 10px rgba(0,0,0,.45)}
  .snap .scene{width:100%;height:100%}
  .snap .tag{position:absolute;bottom:9px;font-family:"Permanent Marker",cursive;font-size:17px;color:var(--white);letter-spacing:1px;text-transform:uppercase;text-shadow:0 0 3px rgba(0,0,0,.6)}
  .tag.right{right:12px}
  .tag.left{left:12px}
  .photo-1 .tag.right{right:34px}

  .scene-after-garden{background:linear-gradient(180deg,#8fb7de 0%,#5f8a4c 35%,#3c6a2c 60%,#4f8f2e 100%)}
  .scene-before-yard{background:linear-gradient(180deg,#b8cfe6 0%,#5e6e4a 40%,#8a8a62 70%,#6d6a58 100%)}
  .scene-after-facade{background:linear-gradient(180deg,#c9dcf0 0%,#6a7590 25%,#565f78 70%,#4f8a37 100%)}
  .scene-before-facade{background:linear-gradient(180deg,#c2d6ec 0%,#e0dccf 30%,#8f7760 60%,#5e6a4a 100%)}
  .scene-after-cottage{background:linear-gradient(180deg,#6fa7e0 0%,#c7d0d6 40%,#a9b1b6 58%,#5aa83a 100%)}
  .scene-before-cottage{background:linear-gradient(180deg,#a4c0dc 0%,#6b5243 35%,#7c7060 65%,#3e4a34 100%)}

  .photo-1{left:258px;top:293px;width:292px;height:210px;transform:rotate(2deg)}
  .photo-2{left:129px;top:454px;width:263px;height:179px;transform:rotate(-.5deg)}
  .chart{position:absolute;left:225px;top:560px;width:320px;height:200px;transform:rotate(-8deg);background:var(--paper);box-shadow:3px 4px 10px rgba(0,0,0,.4)}
  .photo-3{left:528px;top:409px;width:345px;height:230px;transform:rotate(-.5deg)}
  .photo-4{left:506px;top:605px;width:286px;height:198px;transform:rotate(-1.5deg)}
  .photo-5{left:122px;top:729px;width:256px;height:174px;transform:rotate(.5deg)}
  .photo-6{left:429px;top:798px;width:194px;height:128px;transform:rotate(.5deg)}
  .pin-line{position:absolute;left:0;top:0}

  .subtitle{position:absolute;top:941px;left:40px;right:40px;text-align:center;font-size:30px;line-height:1.13;letter-spacing:1px;text-transform:uppercase}
  .imprint{position:absolute;top:1140px;left:0;width:100%;text-align:center;font-family:"Open Sans",Arial,sans-serif;font-size:15px;letter-spacing:2.5px;color:var(--cream)}
</style>
</head>
<body>
<main class="cover">
  <p class="author">Marcus Ellery</p>
  <h1 class="book-title">
    <span class="title title-main">GILDED</span>
    <span class="title title-sub">BRICKWORK</span>
  </h1>

  <figure class="snap photo-1"><div class="scene scene-after-garden" role="img" aria-label="Renovated cottage behind large shade trees with stepping stones across a lawn"></div><span class="tag right">After</span></figure>
  <figure class="snap photo-2"><div class="scene scene-before-yard" role="img" aria-label="Unkempt backyard with dry dirt, trees and an old carport before renovation"></div><span class="tag left">Before</span></figure>

  <div class="chart">
    <svg width="320" height="200" viewBox="0 0 320 200" aria-label="Rising profit line chart">
      <g stroke="var(--rule)" stroke-width="1.5">
        <line x1="12" y1="36" x2="304" y2="36"/>
        <line x1="12" y1="63" x2="304" y2="63"/>
        <line x1="12" y1="90" x2="304" y2="90"/>
        <line x1="12" y1="117" x2="304" y2="117"/>
        <line x1="12" y1="144" x2="304" y2="144"/>
        <line x1="12" y1="171" x2="304" y2="171"/>
        <line x1="14" y1="18" x2="14" y2="182"/>
      </g>
      <polyline points="20,152 84,126 154,92 220,68 292,44" fill="none" stroke="var(--ink)" stroke-width="1.5"/>
      <g fill="var(--ink)">
        <circle cx="20" cy="152" r="3.5"/><circle cx="84" cy="126" r="3.5"/><circle cx="154" cy="92" r="3.5"/><circle cx="220" cy="68" r="3.5"/><circle cx="292" cy="44" r="3.5"/>
      </g>
    </svg>
  </div>

  <figure class="snap photo-3"><div class="scene scene-after-facade" role="img" aria-label="Renovated two-storey home in grey-blue cladding with twin dark garage doors at dusk"></div><span class="tag right">After</span></figure>
  <figure class="snap photo-4"><div class="scene scene-before-facade" role="img" aria-label="Dated cream two-storey home with brick base and concrete driveway before renovation"></div><span class="tag right">Before</span></figure>
  <figure class="snap photo-5"><div class="scene scene-after-cottage" role="img" aria-label="Renovated light grey cottage with verandah on a bright green lawn"></div><span class="tag left">After</span></figure>

  <svg class="pin-line" width="923" height="1200" aria-hidden="true"><line x1="378" y1="847" x2="429" y2="865" stroke="var(--alert-red)" stroke-width="3"/></svg>

  <figure class="snap photo-6"><div class="scene scene-before-cottage" role="img" aria-label="Old raised timber house with front stairs and overgrown garden before renovation"></div><span class="tag right">Before</span></figure>

  <p class="subtitle">The dependable route whereby<br>modest housing flips yield<br>handsome returns</p>
  <p class="imprint">Ellery Dwellings • Build Your Equity</p>
</main>
</body>
</html>
```